Skip Bin Hire Business

We are an existing business that hire out skip bins for domestic and commercial use. We are looking for a fresh look with no colours or designs in mind.
We have 2m3 and 3m3 skip bins and 3m3 up to 24m3 walk in bins.
Visit our website for more information.
www.harbourcrate.com.au
We are going to add a photo of a 3m3 skip as this is a new product for our company and not available on our website at this stage.

Industry/Entity Type

Business

Contact Information for Business Card

Harbour Crate
9218-7046
www.harbourcrate.com.au

```html
<!DOCTYPE html>
<html lang="en">
<head>
<meta charset="utf-8">
<title>Harbour Crate – Business Card</title>
<link rel="stylesheet" href="https://fonts.googleapis.com/css2?family=Michroma&family=Raleway:wght@400;500&display=swap">
<style>
  :root {
    --page-bg: #e9e7e3;
    --card-white: #ffffff;
    --ink: #231f20;
    --band-black: #2a2627;
    --bin-yellow: #f2c200;
    --text-light: #f4f4f4;
  }
  html, body {
    margin: 0;
    padding: 0;
    width: 1200px;
    height: 1000px;
    overflow: hidden;
    background: var(--page-bg);
  }
  .canvas {
    position: relative;
    width: 1200px;
    height: 1000px;
  }
  .business-card {
    position: absolute;
    left: 100px;
    top: 215px;
    width: 1000px;
    height: 570px;
    border-radius: 36px;
    overflow: hidden;
    background: var(--card-white);
    box-shadow: 0 18px 40px rgba(0,0,0,0.18);
  }
  .card-art {
    position: absolute;
    inset: 0;
  }
  .brand-name {
    position: absolute;
    right: 60px;
    top: 58px;
    margin: 0;
    font-family: "Michroma", sans-serif;
    font-weight: 400;
    font-size: 58px;
    letter-spacing: 2px;
    color: var(--ink);
    line-height: 1;
    white-space: nowrap;
  }
  .tagline {
    position: absolute;
    right: 60px;
    top: 150px;
    margin: 0;
    font-family: "Raleway", sans-serif;
    font-weight: 500;
    font-size: 30px;
    color: var(--ink);
    line-height: 1;
    white-space: nowrap;
  }
  .contact-phone {
    position: absolute;
    left: 40px;
    top: 488px;
    font-family: "Raleway", sans-serif;
    font-weight: 400;
    font-size: 48px;
    color: var(--text-light);
    line-height: 1;
    white-space: nowrap;
  }
  .contact-web {
    position: absolute;
    left: 622px;
    top: 396px;
    font-family: "Raleway", sans-serif;
    font-weight: 400;
    font-size: 28px;
    color: var(--text-light);
    line-height: 1;
    white-space: nowrap;
  }
</style>
</head>
<body>
<div class="canvas">
  <div class="business-card">
    <svg class="card-art" width="1000" height="570" viewBox="0 0 1000 570" xmlns="http://www.w3.org/2000/svg">
      <defs>
        <clipPath id="photo-strip-clip">
          <polygon points="0,206 1000,206 1000,332 0,442"/>
        </clipPath>
        <linearGradient id="photo-skip-front" x1="0" y1="0" x2="0" y2="1">
          <stop offset="0" stop-color="#7fa3c4"/>
          <stop offset="0.35" stop-color="#d9a800"/>
          <stop offset="1" stop-color="#8b7a55"/>
        </linearGradient>
        <linearGradient id="photo-skip-side" x1="0" y1="0" x2="0" y2="1">
          <stop offset="0" stop-color="#9a9a92"/>
          <stop offset="0.3" stop-color="#e6b800"/>
          <stop offset="1" stop-color="#7a6a4c"/>
        </linearGradient>
        <linearGradient id="photo-walkin-bin" x1="0" y1="0" x2="0" y2="1">
          <stop offset="0" stop-color="#3f6fb4"/>
          <stop offset="0.45" stop-color="#e0b000"/>
          <stop offset="1" stop-color="#7b5a3c"/>
        </linearGradient>
        <linearGradient id="photo-yard" x1="0" y1="0" x2="0" y2="1">
          <stop offset="0" stop-color="#3d5a3a"/>
          <stop offset="0.45" stop-color="#c9b030"/>
          <stop offset="1" stop-color="#8e8e8e"/>
        </linearGradient>
      </defs>

      <g clip-path="url(#photo-strip-clip)">
        <g role="img" aria-label="Photo of a small yellow skip bin seen from the front corner">
          <rect x="0" y="200" width="200" height="250" fill="url(#photo-skip-front)"/>
        </g>
        <g role="img" aria-label="Photo of a yellow 3m3 skip bin with its side lettering">
          <rect x="200" y="200" width="230" height="250" fill="url(#photo-skip-side)"/>
        </g>
        <g role="img" aria-label="Photo of a long yellow walk-in bin under a blue sky">
          <rect x="430" y="200" width="215" height="250" fill="url(#photo-walkin-bin)"/>
        </g>
        <g role="img" aria-label="Photo of a yellow walk-in bin in a yard with trees and a ute">
          <rect x="645" y="200" width="355" height="250" fill="url(#photo-yard)"/>
        </g>
      </g>

      <polygon class="lower-band" points="0,442 1000,332 1000,570 0,570" fill="var(--band-black)"/>

      <line x1="0" y1="205" x2="1000" y2="205" stroke="var(--bin-yellow)" stroke-width="4"/>
      <line x1="0" y1="442" x2="1000" y2="332" stroke="var(--bin-yellow)" stroke-width="4"/>

      <g class="icon-phone" transform="translate(318,512)">
        <circle r="24" fill="var(--bin-yellow)"/>
        <circle r="20" fill="none" stroke="var(--ink)" stroke-width="1.5"/>
        <rect x="-8" y="-13" width="16" height="26" rx="2.5" fill="none" stroke="var(--ink)" stroke-width="2"/>
        <rect x="-5" y="-9" width="10" height="9" fill="var(--ink)"/>
        <circle cx="-3" cy="5" r="1.3" fill="var(--ink)"/>
        <circle cx="3" cy="5" r="1.3" fill="var(--ink)"/>
        <circle cx="-3" cy="9" r="1.3" fill="var(--ink)"/>
        <circle cx="3" cy="9" r="1.3" fill="var(--ink)"/>
      </g>

      <g class="icon-globe" transform="translate(584,410)">
        <circle r="24" fill="var(--bin-yellow)"/>
        <circle r="20" fill="none" stroke="var(--ink)" stroke-width="1.5"/>
        <circle r="13" fill="none" stroke="var(--ink)" stroke-width="2"/>
        <ellipse rx="6" ry="13" fill="none" stroke="var(--ink)" stroke-width="1.6"/>
        <line x1="-13" y1="0" x2="13" y2="0" stroke="var(--ink)" stroke-width="1.6"/>
        <line x1="-11" y1="-6" x2="11" y2="-6" stroke="var(--ink)" stroke-width="1.4"/>
        <line x1="-11" y1="6" x2="11" y2="6" stroke="var(--ink)" stroke-width="1.4"/>
      </g>
    </svg>

    <h1 class="brand-name">HARBOUR CRATE</h1>
    <p class="tagline">2m3 and 3m3 skip bins and 3m3 up to 24m3 walk in bins</p>
    <div class="contact-web">www.harbourcrate.com.au</div>
    <div class="contact-phone">9218-7046</div>
  </div>
</div>
</body>
</html>
```